Jewelry Shop Needs a Business Card Design

***We want a very sharp and unforgettable pantone for the Business Card. ***
***We do not want the business card or logo only in black, white and grey color!!!Please provide us a main color as our brand topic! Thanks!! ***

Mabel’s Nook is a Hong Kong based fine jewelry brand.

We want a very nice, simple and elegant business card design for Mabel's Nook Brand. The company's logo has been uploaded already.

You can design with below info:

Dorian Fung
Director
M: +852 94273658
T: +852 35820417
F: +852 35820419
E: dorian.fung@mabelsnook.example
5/F , Harbourlight Tower, 12-18 Orchid Lane, Wan Tung Kok, Kowloon, Hong Kong

Target Market(s)

Mabel’s Nook philosophy is a jewelry icon of young, creative, trendy, fashionable, stylish, energetic, and elegant. For Mabel’s Nook, jewelry is one collection of artworks, the most important items in personal life.

Industry/Entity Type

Jewelry

Requirements
Must have
• We want a very sharp and unforgettable pantone for the Business Card.

```html
<!DOCTYPE html>
<html lang="en">
<head>
<meta charset="UTF-8">
<title>Mabel's Nook – Business Card</title>
<link rel="stylesheet" href="https://fonts.googleapis.com/css2?family=Cinzel:wght@600&family=Arimo:wght@400&display=swap">
<style>
  :root {
    --stage: #1e1e1e;
    --card-white: #ffffff;
    --card-white-edge: #f1f1f1;
    --gold-light: #ffd23a;
    --gold: #fcc21b;
    --gold-deep: #f4b10c;
    --ink: #111111;
    --rule: rgba(90, 60, 0, 0.45);
  }
  * { margin: 0; padding: 0; box-sizing: border-box; }
  html, body {
    width: 1200px;
    height: 750px;
    overflow: hidden;
    background: var(--stage);
  }
  .stage {
    width: 1200px;
    height: 750px;
    display: flex;
    align-items: center;
    justify-content: center;
    gap: 50px;
  }
  .card {
    width: 525px;
    height: 300px;
    border-radius: 18px;
    position: relative;
    display: flex;
    flex-direction: column;
    align-items: center;
    color: var(--ink);
    box-shadow: 0 10px 30px rgba(0,0,0,0.45);
  }
  .card--front {
    background: linear-gradient(160deg, var(--card-white), var(--card-white-edge));
    justify-content: center;
  }
  .card--back {
    background: linear-gradient(150deg, var(--gold-light) 0%, var(--gold) 55%, var(--gold-deep) 100%);
    padding: 0 40px;
  }
  .brand-dot {
    width: 72px;
    height: 72px;
    border-radius: 50%;
    background: var(--ink);
  }
  .brand-name {
    font-family: 'Cinzel', serif;
    font-weight: 600;
    font-size: 17px;
    letter-spacing: 1.5px;
    margin-top: 14px;
    color: var(--ink);
  }
  .website {
    font-family: 'Arimo', sans-serif;
    font-size: 12px;
    margin-top: 42px;
    color: #333333;
  }
  .rule {
    width: 100%;
    height: 1px;
    background: var(--rule);
  }
  .rule--top { margin-top: 22px; }
  .card--back .brand-dot { margin-top: 14px; width: 66px; height: 66px; }
  .card--back .brand-name { margin-top: 10px; font-size: 16px; }
  .person {
    font-family: 'Arimo', sans-serif;
    font-size: 13px;
    margin-top: 6px;
  }
  .role {
    font-family: 'Arimo', sans-serif;
    font-size: 9px;
    margin-top: 2px;
    margin-bottom: 12px;
  }
  .address {
    font-family: 'Arimo', sans-serif;
    font-size: 10px;
    line-height: 1.4;
    text-align: center;
    margin-top: 12px;
  }
  .contacts {
    font-family: 'Arimo', sans-serif;
    font-size: 10px;
    margin-top: 10px;
    margin-bottom: 10px;
    white-space: nowrap;
  }
  .contacts .sep { font-weight: 700; padding: 0 3px; }
</style>
</head>
<body>
  <main class="stage">
    <section class="card card--front" aria-label="Card front">
      <div class="brand-dot"></div>
      <div class="brand-name">Mabel’s Nook</div>
      <div class="website">www.mabelsnook.example</div>
    </section>

    <section class="card card--back" aria-label="Card back">
      <div class="rule rule--top"></div>
      <div class="brand-dot"></div>
      <div class="brand-name">Mabel’s Nook</div>
      <div class="person">Dorian Fung</div>
      <div class="role">Director</div>
      <div class="rule"></div>
      <p class="address">
        5/F , Harbourlight Tower, 12-18 Orchid Lane,<br>
        Wan Tung Kok, Kowloon, Hong Kong
      </p>
      <p class="contacts">
        +852 94273658<span class="sep">|</span>+852 35820417<span class="sep">|</span>+852 35820419<span class="sep">|</span>dorian.fung@mabelsnook.example
      </p>
      <div class="rule"></div>
    </section>
  </main>
</body>
</html>
```